Design a cover for a new book!

Design a cover for a new book called "The Ledger and the Lathe" Subtitle is "A Fresh Monetary Blueprint Built For Modern Working Households"

The brief attached will give you the theme of the book. The book tells how there are two economies, one controlled by people who own financial assets, and the other run by people who build real things that contribute to our standard of living.

We want a split cover showing two different economies existing at the same time. The cover should show a split scene! Half the cover should be the monetary economy - the stock market or derivative or commodities. The other half the cover should show the material economy - technology and manufacturing, or maybe people living and doing things.

Target Market(s)

General Audience, people who like political policy

Industry/Entity Type

economics

Requirements
Must have
• The cover should show a split scene! Half the cover should be the monetary economy - the stock market or derivative or commodities. The other half the cover should show the material economy - technology and manufacturing,

```html
<!DOCTYPE html>
<html lang="en">
<head>
<meta charset="utf-8">
<title>The Ledger and the Lathe – Book Cover</title>
<link href="https://fonts.googleapis.com/css2?family=Bebas+Neue&family=Montserrat:wght@500&display=swap" rel="stylesheet">
<style>
  :root {
    --canvas-bg: #eceded;
    --paper: #f4f4f4;
    --paper-shade: #bdbdbd;
    --ink-dark: #1c1c1c;
    --title-white: #ffffff;
    --market-deep: #0d3f73;
    --market-mid: #1d6aa8;
    --market-glow: #2fa3d6;
    --chart-grid: rgba(120, 210, 255, 0.22);
    --chart-line: #6fe3ff;
    --chart-up: #3fe0a8;
    --chart-down: #e0566a;
    --chart-trend: #e07a5a;
    --port-sky: #6a6fb0;
    --port-sun: #f0a35a;
    --port-ground: #3a4a63;
    --placeholder-mark: rgba(255, 255, 255, 0.28);
  }
  * { margin: 0; padding: 0; box-sizing: border-box; }
  html, body {
    width: 1200px;
    height: 1200px;
    overflow: hidden;
    background: var(--canvas-bg);
  }
  .canvas {
    position: relative;
    width: 1200px;
    height: 1200px;
    display: flex;
    justify-content: center;
  }
  .book-cover {
    position: relative;
    width: 768px;
    height: 1200px;
    overflow: hidden;
    background: var(--market-deep);
  }
  .market-scene {
    position: absolute;
    left: 0; top: 140px;
    width: 100%; height: 600px;
    background:
      radial-gradient(ellipse at 50% 15%, var(--market-glow) 0%, transparent 60%),
      linear-gradient(180deg, var(--market-mid) 0%, var(--market-deep) 70%, #16548c 100%);
  }
  .market-chart {
    position: absolute;
    left: 0; top: 0;
    width: 100%; height: 100%;
  }
  .port-scene {
    position: absolute;
    left: 0; top: 720px;
    width: 100%; height: 480px;
    background:
      radial-gradient(ellipse at 50% 62%, #ffd38a 0%, var(--port-sun) 16%, transparent 42%),
      linear-gradient(180deg, rgba(22,84,140,0) 0%, var(--port-sky) 22%, #b77a8e 48%, #7a5a5e 66%, var(--port-ground) 84%, #35455c 100%);
  }
  .photo-placeholder {
    position: absolute;
    left: 0; top: 0;
    width: 100%; height: 100%;
  }
  .torn-header {
    position: absolute;
    left: 0; top: 0;
    width: 100%; height: 220px;
  }
  .subtitle {
    position: absolute;
    left: 0; top: 30px;
    width: 100%;
    text-align: center;
    font-family: "Montserrat", sans-serif;
    font-weight: 500;
    font-size: 24px;
    line-height: 38px;
    letter-spacing: 0.15em;
    text-transform: uppercase;
    color: var(--ink-dark);
  }
  .title {
    position: absolute;
    left: 0; top: 352px;
    width: 100%;
    text-align: center;
    font-family: "Bebas Neue", sans-serif;
    font-weight: 400;
    font-size: 180px;
    line-height: 146px;
    color: var(--title-white);
    text-transform: uppercase;
  }
  .title span { display: block; }
  .author {
    position: absolute;
    left: 0; bottom: 34px;
    width: 100%;
    text-align: center;
    font-family: "Montserrat", sans-serif;
    font-weight: 500;
    font-size: 42px;
    letter-spacing: 0.14em;
    color: var(--title-white);
    text-transform: uppercase;
  }
</style>
</head>
<body>
<div class="canvas">
  <div class="book-cover">
    <div class="market-scene" role="img" aria-label="Glowing blue stock market candlestick and line charts over financial district buildings">
      <svg class="market-chart" viewBox="0 0 768 600" preserveAspectRatio="none" aria-hidden="true">
        <g stroke="var(--chart-grid)" stroke-width="1">
          <line x1="0" y1="80" x2="768" y2="80"/>
          <line x1="0" y1="140" x2="768" y2="140"/>
          <line x1="0" y1="200" x2="768" y2="200"/>
          <line x1="0" y1="260" x2="768" y2="260"/>
          <line x1="0" y1="320" x2="768" y2="320"/>
          <line x1="0" y1="380" x2="768" y2="380"/>
          <line x1="96" y1="40" x2="96" y2="480"/>
          <line x1="192" y1="40" x2="192" y2="480"/>
          <line x1="288" y1="40" x2="288" y2="480"/>
          <line x1="384" y1="40" x2="384" y2="480"/>
          <line x1="480" y1="40" x2="480" y2="480"/>
          <line x1="576" y1="40" x2="576" y2="480"/>
          <line x1="672" y1="40" x2="672" y2="480"/>
        </g>
        <g stroke-width="2">
          <line x1="20" y1="210" x2="20" y2="290" stroke="var(--chart-up)"/><rect x="15" y="225" width="10" height="50" fill="var(--chart-up)"/>
          <line x1="48" y1="250" x2="48" y2="330" stroke="var(--chart-down)"/><rect x="43" y="262" width="10" height="48" fill="var(--chart-down)"/>
          <line x1="76" y1="200" x2="76" y2="290" stroke="var(--chart-up)"/><rect x="71" y="215" width="10" height="55" fill="var(--chart-up)"/>
          <line x1="104" y1="220" x2="104" y2="300" stroke="var(--chart-up)"/><rect x="99" y="232" width="10" height="52" fill="var(--chart-up)"/>
          <line x1="132" y1="190" x2="132" y2="270" stroke="var(--chart-down)"/><rect x="127" y="205" width="10" height="45" fill="var(--chart-down)"/>
          <line x1="160" y1="150" x2="160" y2="240" stroke="var(--chart-up)"/><rect x="155" y="165" width="10" height="58" fill="var(--chart-up)"/>
          <line x1="188" y1="170" x2="188" y2="250" stroke="var(--chart-up)"/><rect x="183" y="182" width="10" height="50" fill="var(--chart-up)"/>
          <line x1="216" y1="120" x2="216" y2="200" stroke="var(--chart-down)"/><rect x="211" y="132" width="10" height="48" fill="var(--chart-down)"/>
          <line x1="244" y1="140" x2="244" y2="220" stroke="var(--chart-up)"/><rect x="239" y="152" width="10" height="50" fill="var(--chart-up)"/>
          <line x1="272" y1="100" x2="272" y2="180" stroke="var(--chart-up)"/><rect x="267" y="112" width="10" height="48" fill="var(--chart-up)"/>
          <line x1="470" y1="60" x2="470" y2="140" stroke="var(--chart-down)"/><rect x="465" y="72" width="10" height="45" fill="var(--chart-down)"/>
          <line x1="498" y1="50" x2="498" y2="130" stroke="var(--chart-up)"/><rect x="493" y="62" width="10" height="48" fill="var(--chart-up)"/>
          <line x1="526" y1="40" x2="526" y2="120" stroke="var(--chart-up)"/><rect x="521" y="52" width="10" height="46" fill="var(--chart-up)"/>
          <line x1="554" y1="55" x2="554" y2="130" stroke="var(--chart-down)"/><rect x="549" y="66" width="10" height="42" fill="var(--chart-down)"/>
        </g>
        <polyline fill="none" stroke="var(--chart-line)" stroke-width="2.5" points="0,250 40,230 80,260 120,200 160,215 200,170 240,190 280,140 320,150 360,110 400,130 440,90 480,100 520,60 560,80 600,70 640,110 680,90 720,120 768,100"/>
        <polyline fill="none" stroke="var(--chart-trend)" stroke-width="1.5" points="300,40 340,70 380,60 420,110 460,90 500,140 540,130 580,100 610,160 640,200 670,230 700,215 730,150 768,120"/>
      </svg>
    </div>

    <div class="port-scene" role="img" aria-label="Shipping port at sunset with container stacks, cranes, cargo ship, trucks and a departing airplane">
      <svg class="photo-placeholder" viewBox="0 0 768 480" preserveAspectRatio="none" aria-hidden="true">
        <g fill="none" stroke="var(--placeholder-mark)" stroke-width="2" stroke-dasharray="10 8">
          <rect x="24" y="90" width="720" height="290"/>
          <line x1="24" y1="90" x2="744" y2="380"/>
          <line x1="744" y1="90" x2="24" y2="380"/>
        </g>
      </svg>
    </div>

    <svg class="torn-header" viewBox="0 0 768 220" preserveAspectRatio="none" aria-hidden="true">
      <path fill="var(--paper-shade)" d="M0 0 H768 V170 L742 176 L716 162 L690 180 L664 166 L636 184 L606 170 L580 190 L552 176 L526 186 L496 168 L466 192 L436 178 L406 186 L378 166 L346 188 L316 176 L288 196 L256 178 L226 188 L196 172 L166 194 L136 180 L104 198 L74 182 L44 192 L0 180 Z"/>
      <path fill="var(--paper)" d="M0 0 H768 V158 L744 164 L718 150 L692 168 L664 154 L638 172 L608 158 L582 176 L554 162 L528 172 L498 156 L468 178 L438 164 L408 172 L380 154 L348 174 L318 162 L290 182 L258 164 L228 174 L198 158 L168 180 L138 166 L106 184 L76 168 L46 178 L0 166 Z"/>
    </svg>

    <p class="subtitle">A Fresh Monetary Blueprint Built<br>For Modern Working Households</p>

    <h1 class="title">
      <span>The Ledger</span>
      <span>And The</span>
      <span>Lathe</span>
    </h1>

    <p class="author">Daniel Reed Hollis</p>
  </div>
</div>
</body>
</html>
```